Psychic event planner needs a poster design for psychic fair

I need a poster design for a psychic event based in Victoria, B.C., Canada. This psychic fair is a unique blend of Native American with New Age/Metaphysical. All the practitioners, from psychic, spiritual readers to healers are Native American and practice New Age. This event is open to the general public.

Target Market(s)

18-45 year old women

Industry/Entity Type

Event

Font styles to use
Other font styles liked:
• The font I like is called Blue Plate Special NF to be used for the name of the fair, "The Cedar Moon Gathering Expo" Below is the link to download: http://www.typevault-example.com/font-download-page.html

Requirements
Must have
• You must be good with Illustration.
• Size: 8.5 by 11
• DPI: 300
• All the below text must be used:
• The Cedar Moon Gathering Expo
• Walk Where Lanterns Glow
• Elders Psychic Medium Traditional Healing
• Metaphysical Tarot Wisdom Holistic Health
• 45 vendors selling crystals, traditional jewelry and more
• Admission: $5 - Services start at $25
• Location: Harlow Ridge Community School Centre, 327 Dunmore St, Victoria, BC
• velmarostudio.example-site.com/
• Call Corinne Vantaro for info : 778-555-0164
• The illustrated poster needs to be a blend of New Age and Native American. Should look bold, colourful, spiritual
• I found a poster that I like, the file is below
• remove the horse and replace it with a canoe.
• The canoe must look like it's rearing like it's moving through water rapids.
• Remove the snake. Feminize the man and turn it into a woman minus the war paint.
• Have her hair big and wild with crystals, and shells instead of the fish.
• Main headline, The Cedar Moon Gathering Expo
• Walk Where Lanterns Glow, must be in the font called Blue Plate Special NF.
• The rest of the txt in Helvetica.
• You are welcome to place the text in whatever appealing way you like.
• Logo:
• My logo the frog can be changed to one of the turquoise blues you choose to use. The logo file is attached below
• Files are named:
Should not have
• No arrows, no pentagrams.
• No Maori (Indigenous from New Zealand) and no Inuit (Eskimo tattoos), no other tribal tattoos to be used.
• No sexy attire.

```html
<!DOCTYPE html>
<html lang="en">
<head>
<meta charset="utf-8">
<title>The Cedar Moon Gathering Expo</title>
<link rel="stylesheet" href="https://fonts.googleapis.com/css2?family=Permanent+Marker&family=Berkshire+Swash&family=Caveat:wght@500;700&family=Amatic+SC:wght@700&family=Archivo:wght@700;800&display=swap">
<style>
  :root {
    --tan: #c99f7b;
    --tan-light: #d9bfa6;
    --frame: #4b2a29;
    --panel: #f2f1f8;
    --ink: #141010;
    --white: #ffffff;
    --canoe: #d9a94f;
    --dress: #b47a2a;
    --web-red: #d9405c;
    --badge: #2f2a29;
  }
  html, body { margin: 0; padding: 0; overflow: hidden; background: var(--white); }
  .poster {
    position: relative;
    width: 834px;
    height: 1200px;
    overflow: hidden;
    background: var(--white);
  }
  .layer { position: absolute; inset: 0; }
  .abs { position: absolute; margin: 0; }

  .marker { font-family: "Permanent Marker", cursive; text-transform: uppercase; }
  .headline-text {
    fill: var(--ink);
    stroke: var(--white);
    stroke-width: 10px;
    stroke-linejoin: round;
    paint-order: stroke fill;
  }
  .tagline-text { fill: var(--ink); }
  .badge-text { fill: var(--panel); }
  .contact-text { font-family: "Amatic SC", sans-serif; font-weight: 700; fill: var(--ink); }

  .illustration {
    left: 132px; top: 262px; width: 590px; height: 400px;
    background: radial-gradient(ellipse at 50% 55%, var(--dress) 0%, var(--canoe) 40%, rgba(217,169,79,0.35) 70%, rgba(242,241,248,0) 100%);
    border-radius: 40% 40% 30% 30%;
  }
  .studio-mark {
    left: 500px; top: 300px;
    display: flex; align-items: center; gap: 6px;
    font-family: "Archivo", Arial, sans-serif; font-weight: 800;
    font-size: 15px; color: var(--ink); white-space: nowrap;
  }
  .studio-mark .dot { width: 11px; height: 11px; border-radius: 50%; background: var(--ink); }

  .services { left: 172px; top: 814px; width: 400px; list-style: none; padding: 0; }
  .services li {
    position: relative; padding-left: 30px; margin-bottom: 8px;
    font-family: "Berkshire Swash", serif; font-size: 24px; line-height: 1.1; color: var(--ink);
    white-space: nowrap;
  }
  .services li::before {
    content: ""; position: absolute; left: 4px; top: 10px;
    width: 12px; height: 12px; border-radius: 50%; background: var(--ink);
  }

  .vendors {
    left: 202px; top: 946px; width: 200px;
    font-family: "Caveat", cursive; font-weight: 500;
    font-size: 17px; line-height: 1.1; color: var(--ink);
  }

  .pricing { left: 410px; top: 940px; width: 300px; font-family: "Caveat", cursive; font-weight: 500; color: var(--ink); line-height: 1.1; white-space: nowrap; }
  .pricing .admission { font-size: 32px; }
  .pricing .services-price { font-size: 26px; }

  .venue {
    left: 150px; top: 1110px; width: 560px;
    font-family: "Archivo", Arial, sans-serif; font-weight: 700; font-style: normal;
    font-size: 18px; line-height: 1.3; letter-spacing: 1.2px; color: var(--white);
  }
  .website {
    right: 26px; bottom: 2px;
    font-family: "Archivo", Arial, sans-serif; font-weight: 800;
    font-size: 19px; letter-spacing: 0.5px; color: var(--web-red);
    paint-order: stroke fill; -webkit-text-stroke: 4px var(--white);
    white-space: nowrap;
  }
</style>
</head>
<body>
<main class="poster">
  <svg class="layer" width="834" height="1200" viewBox="0 0 834 1200" aria-hidden="true">
    <rect x="24" y="6" width="786" height="1186" fill="var(--tan)"/>
    <rect x="0" y="160" width="30" height="880" fill="var(--tan-light)"/>
    <rect x="120" y="60" width="662" height="1108" fill="var(--frame)"/>
    <rect x="160" y="40" width="596" height="1066" fill="var(--panel)"/>
    <line x1="175" y1="800" x2="560" y2="798" stroke="#d6d3dd" stroke-width="2"/>
  </svg>

  <div class="abs illustration" role="img" aria-label="Illustration of a woman with long dark hair in a fringed dress, paddling a golden canoe"></div>

  <svg class="layer" width="834" height="1200" viewBox="0 0 834 1200">
    <g class="marker headline-text">
      <text x="92" y="100" font-size="54" textLength="240" lengthAdjust="spacingAndGlyphs">The Cedar</text>
      <text x="66" y="188" font-size="84" textLength="700" lengthAdjust="spacingAndGlyphs">Moon Gathering</text>
      <text x="590" y="284" font-size="92" textLength="180" lengthAdjust="spacingAndGlyphs">Expo</text>
    </g>
    <g class="marker tagline-text" text-anchor="middle">
      <text x="425" y="718" font-size="56" textLength="380" lengthAdjust="spacingAndGlyphs">Walk Where</text>
      <text x="425" y="778" font-size="56" textLength="300" lengthAdjust="spacingAndGlyphs">Lanterns Glow</text>
    </g>
    <g>
      <circle cx="665" cy="770" r="74" fill="var(--tan-light)"/>
      <circle cx="665" cy="770" r="57" fill="var(--badge)"/>
      <g class="marker badge-text" text-anchor="middle">
        <text x="665" y="763" font-size="30" textLength="84" lengthAdjust="spacingAndGlyphs">June</text>
        <text x="665" y="800" font-size="30" textLength="50" lengthAdjust="spacingAndGlyphs">2&amp;3</text>
      </g>
    </g>
    <g class="contact-text">
      <text x="132" y="1036" font-size="40" textLength="60" lengthAdjust="spacingAndGlyphs">CALL</text>
      <text x="164" y="1080" font-size="40" textLength="212" lengthAdjust="spacingAndGlyphs">CORINNE VANTARO</text>
      <text x="384" y="1080" font-size="22" textLength="66" lengthAdjust="spacingAndGlyphs">FOR INFO</text>
      <text x="464" y="1084" font-size="58" textLength="282" lengthAdjust="spacingAndGlyphs">778-555-0164</text>
    </g>
  </svg>

  <div class="abs studio-mark"><span class="dot"></span>Velmaro Studio</div>

  <ul class="abs services">
    <li>Elders Psychic Medium<br>Traditional Healing</li>
    <li>Metaphysical Tarot Wisdom<br>Holistic Health</li>
  </ul>

  <p class="abs vendors">45 vendors selling crystals, traditional jewelry and more</p>

  <div class="abs pricing">
    <div class="admission">Admission: $5</div>
    <div class="services-price">Services start at $25</div>
  </div>

  <address class="abs venue">Harlow Ridge Community School Centre,<br>327 Dunmore St, Victoria, BC</address>
  <p class="abs website">velmarostudio.example-site.com</p>
</main>
</body>
</html>
```